Menu Board 1000mmx500mm re-design

I would like to re-design exiting menu board 1000mmx500mm. Current board letters are bit to small to read. I would like to have pictures (attached) of the food offered on it and at the same time to create balance between pictures and size of the text to be easily readable. Fonts and colours are up to designer choice but prefer warm and bright colours rather anything dark.

Target Market(s)

Food industry

Industry/Entity Type

Food

Font styles to use
Other font styles liked:
• I leave font choice to designer

Colors
FFC000
F8CF3A
FAE287
FDF2CF
FEFAEE
F0912C
F2A743
F7CA91
FBE8D2
FDF5EE
EE7325
F08F49
F5BC92
FAE3D3
FDF4ED

Requirements
Must have
• Pictures + Text
Nice to have
• Balance between images and text.
Should not have
• Can't think of any

```html
<!DOCTYPE html>
<html lang="en">
<head>
<meta charset="utf-8">
<title>Menu Board</title>
<link rel="stylesheet" href="https://fonts.googleapis.com/css2?family=Bebas+Neue&family=Kaushan+Script&family=Montserrat:ital,wght@0,500;0,600;1,800&display=swap">
<style>
  :root {
    --orange: #EE7325;
    --orange-deep: #E5601A;
    --orange-soft: #F0912C;
    --amber: #F2A743;
    --cream: #FDF4ED;
    --ink: #111111;
    --text: #3a3a3a;
    --white: #ffffff;
    --backdrop: #f3ede6;
  }
  * { margin: 0; padding: 0; box-sizing: border-box; }
  html, body { width: 782px; height: 1200px; overflow: hidden; background: var(--backdrop); }
  .canvas { position: relative; width: 782px; height: 1200px; overflow: hidden; }
  .board {
    position: absolute; left: 94px; top: 13px;
    width: 1024px; height: 2024px;
    transform: scale(0.58); transform-origin: top left;
    background: var(--white);
    overflow: hidden;
    box-shadow: 0 6px 30px rgba(0,0,0,0.18);
  }
  .board__art { position: absolute; inset: 0; width: 1024px; height: 2024px; }
  .title {
    position: absolute; left: 56px; top: 418px;
    font-family: "Bebas Neue", sans-serif; font-size: 168px; line-height: 1;
    letter-spacing: 10px; color: var(--orange-deep);
  }
  .item-name {
    position: absolute; font-family: "Kaushan Script", cursive;
    font-size: 62px; line-height: 1; color: var(--ink); white-space: nowrap;
  }
  .item-name::before {
    content: ""; position: absolute; left: -24px; top: 32px;
    width: 9px; height: 9px; border-radius: 50%; background: var(--orange);
  }
  .price {
    position: absolute; font-family: "Bebas Neue", sans-serif;
    font-size: 78px; line-height: 1; color: var(--orange-deep); white-space: nowrap;
  }
  .price--inline { font-size: 70px; }
  .desc {
    position: absolute; font-family: "Montserrat", sans-serif; font-weight: 500;
    font-size: 23px; line-height: 30px; color: var(--text); white-space: nowrap;
  }
  .desc--tight { line-height: 27px; }
  .sauces-title {
    position: absolute; left: 550px; top: 1326px;
    font-family: "Kaushan Script", cursive; font-size: 70px; line-height: 1; color: var(--ink);
  }
  .sauce {
    position: absolute; font-family: "Montserrat", sans-serif; font-style: italic;
    font-weight: 800; font-size: 27px; line-height: 1; color: var(--orange-deep);
    letter-spacing: 0.5px; white-space: nowrap;
  }
</style>
</head>
<body>
<div class="canvas">
  <div class="board">
    <svg class="board__art" viewBox="0 0 1024 2024" xmlns="http://www.w3.org/2000/svg">
      <defs>
        <linearGradient id="wrapTone" x1="0" y1="0" x2="1" y2="1">
          <stop offset="0" stop-color="#d9c3a0"/><stop offset="0.5" stop-color="#7a8f3a"/><stop offset="1" stop-color="#c8462c"/>
        </linearGradient>
        <linearGradient id="chickenTone" x1="0" y1="0" x2="1" y2="1">
          <stop offset="0" stop-color="#c88a3e"/><stop offset="0.6" stop-color="#a4642a"/><stop offset="1" stop-color="#6b3f1d"/>
        </linearGradient>
        <linearGradient id="sandwichTone" x1="0" y1="0" x2="1" y2="1">
          <stop offset="0" stop-color="#d8a060"/><stop offset="0.55" stop-color="#6f9a3c"/><stop offset="1" stop-color="#a8304a"/>
        </linearGradient>
        <linearGradient id="potatoTone" x1="0" y1="0" x2="1" y2="1">
          <stop offset="0" stop-color="#e6b04a"/><stop offset="0.6" stop-color="#d69436"/><stop offset="1" stop-color="#5a5e66"/>
        </linearGradient>
      </defs>

      <!-- top orange field -->
      <path d="M12,12 H1012 V706 C860,712 720,640 620,520 C540,420 440,360 310,366 C190,372 90,420 12,462 Z" fill="var(--orange)"/>
      <path d="M12,470 C120,400 240,370 330,372 C460,376 560,470 640,570 C730,690 880,740 1012,716" fill="none" stroke="var(--white)" stroke-width="26"/>
      <path d="M40,440 C150,380 260,350 360,356 C480,364 560,460 650,570" fill="none" stroke="var(--amber)" stroke-width="3"/>
      <path d="M560,520 C650,640 780,760 1012,700" fill="none" stroke="var(--amber)" stroke-width="3"/>

      <!-- wrap photo -->
      <ellipse cx="210" cy="150" rx="232" ry="172" fill="var(--white)"/>
      <ellipse cx="210" cy="150" rx="220" ry="160" fill="url(#wrapTone)" role="img" aria-label="Photo of a grilled chicken wrap with spinach, tomato and onion"/>

      <!-- chicken photo -->
      <circle cx="800" cy="280" r="344" fill="var(--white)"/>
      <circle cx="800" cy="280" r="328" fill="url(#chickenTone)" role="img" aria-label="Photo of a roast chicken quarter with veggie rice"/>

      <!-- right side rings -->
      <path d="M1012,1254 A140,140 0 0 0 1012,1434" fill="none" stroke="var(--orange)" stroke-width="14"/>
      <path d="M1012,1290 A100,100 0 0 0 1012,1400" fill="none" stroke="var(--orange-soft)" stroke-width="3"/>
      <path d="M1012,1316 A60,60 0 0 0 1012,1376" fill="none" stroke="var(--orange-soft)" stroke-width="2"/>

      <!-- sandwich photo -->
      <path d="M12,1470 C60,1420 200,1410 300,1460 C420,1470 450,1580 430,1650 C380,1700 320,1820 200,1846 C120,1860 40,1840 12,1800 Z" fill="url(#sandwichTone)" role="img" aria-label="Photo of a ciabatta sandwich and beetroot wraps with salad"/>
      <path d="M60,1740 C120,1880 330,1930 410,1800" fill="none" stroke="var(--orange-soft)" stroke-width="1.5"/>
      <path d="M30,1760 C100,1930 360,1960 440,1790" fill="none" stroke="var(--orange-soft)" stroke-width="1.5"/>

      <!-- bottom left rings -->
      <path d="M12,1934 C80,1910 150,1960 160,2012" fill="none" stroke="var(--orange)" stroke-width="14"/>
      <path d="M12,1966 C60,1952 110,1980 120,2012" fill="none" stroke="var(--orange-soft)" stroke-width="3"/>

      <!-- potatoes photo -->
      <path d="M400,2012 C410,1780 600,1610 860,1612 C930,1612 980,1620 1012,1640 V2012 Z" fill="var(--orange)"/>
      <path d="M420,2012 C440,1800 620,1660 850,1660 C920,1660 980,1670 1012,1690 V2012 Z" fill="url(#potatoTone)" role="img" aria-label="Photo of roasted potatoes with thyme and garlic"/>

      <!-- white frame -->
      <rect x="6" y="6" width="1012" height="2012" fill="none" stroke="var(--white)" stroke-width="12"/>
    </svg>

    <div class="title">MENU</div>

    <div class="item-name" style="left:82px; top:606px;">Ciabatta</div>
    <div class="price" style="left:72px; top:686px;">£6</div>
    <div class="desc" style="left:154px; top:680px;">Roti Chicken, Rucola,<br>Caramelized Onions,<br>Tomato, Fresh Onion</div>

    <div class="item-name" style="left:86px; top:808px;">Wrap</div>
    <div class="price" style="left:70px; top:902px;">£7</div>
    <div class="desc" style="left:154px; top:890px;">Roti Chicken, Crunchy<br>slaw, tomato, Fresh Onion,<br>sauce of your choice</div>

    <div class="item-name" style="left:82px; top:1040px;">Beetroot Wrap</div>
    <div class="price" style="left:70px; top:1136px;">£8</div>
    <div class="desc" style="left:158px; top:1124px;">Roti Chicken, Crunchy<br>slaw, tomato, Fresh Onion,<br>sauce of your choice</div>

    <div class="item-name" style="left:74px; top:1272px;">Water Can <span class="price price--inline" style="position:static; margin-left:14px;">£1</span></div>
    <div class="item-name" style="left:74px; top:1338px;">&amp; Juice <span class="price price--inline" style="position:static; margin-left:24px;">£1.8</span></div>

    <div class="item-name" style="left:560px; top:754px;">1/4 Chicken Box</div>
    <div class="price" style="left:556px; top:824px;">£9</div>
    <div class="desc desc--tight" style="left:634px; top:834px;">Roti Chicken, Veggie<br>&amp; Salad</div>

    <div class="item-name" style="left:558px; top:960px;">1/2 Chicken Box</div>
    <div class="price" style="left:552px; top:1034px;">£14</div>
    <div class="desc desc--tight" style="left:651px; top:1046px;">Roti Chicken, Veggie Rice<br>&amp; Salad</div>

    <div class="item-name" style="left:558px; top:1164px;">Roasted Potatoes</div>
    <div class="price" style="left:552px; top:1230px;">£2.5</div>
    <div class="desc" style="left:675px; top:1250px;">Thyme &amp; Garlic</div>

    <div class="sauces-title">Sauces</div>
    <div class="sauce" style="left:552px; top:1438px;">SIGNATURE</div>
    <div class="sauce" style="left:810px; top:1440px;">PIRI PIRI</div>
    <div class="sauce" style="left:552px; top:1486px;">SWEET CHILLI</div>
    <div class="sauce" style="left:810px; top:1486px;">BBQ</div>
    <div class="sauce" style="left:550px; top:1534px;">GARLIC MAYO</div>
  </div>
</div>
</body>
</html>
```